Software company needs a web design

We need a web design for the main page of our company, called Brixel Software (where Brixel goes for Brisk Pixel Firm). We develop and sell software for SME as well as Corporate sector within whole European continent.
Our main products are now OVN 7, an (real estate) asset management software enabling efficient management of commercial real estates; DUNE, software for loan management and two HR applications.
As our philosophy is efficiency, focusing on substance, getting rid of cumulated ballast etc., we'd like the web showing the same, i.e. being simple intuitive, rather visual then having too much text but still presenting our products (and our company via them) properly.
People visiting the web should easily find the right information on the company, people behind and our products as well as getting the right impression on what we aim to.
Attached is our company logo.

```html
<!DOCTYPE html>
<html lang="en">
<head>
<meta charset="utf-8">
<title>Brixel Software</title>
<link href="https://fonts.googleapis.com/css2?family=Montserrat:wght@400;500;600;700&display=swap" rel="stylesheet">
<style>
:root{
  --blue:#1b93d1;
  --blue-deep:#0e7fc0;
  --ink:#262a48;
  --text:#8a90a6;
  --soft:#f3f5fa;
  --line:#e6e9f1;
  --navy:#262b4d;
  --white:#ffffff;
}
*{box-sizing:border-box;margin:0;padding:0}
html,body{width:1200px;height:4045px;overflow:hidden;background:var(--white)}
body{font-family:'Montserrat',sans-serif;color:var(--ink);position:relative}
.abs{position:absolute}
.bg-wave{position:absolute;left:0;width:1200px}
.hero-blob{position:absolute;left:0;top:0}
.header{position:absolute;top:22px;left:235px;width:730px;height:48px;display:flex;align-items:center}
.logo{font-weight:600;font-size:22px;color:var(--ink);display:flex;align-items:center;gap:8px;white-space:nowrap}
.logo-square{width:12px;height:12px;background:var(--blue)}
.nav{position:absolute;left:262px;display:flex;gap:10px;font-size:10.5px;font-weight:600;color:var(--ink);white-space:nowrap}
.btn{display:inline-flex;align-items:center;justify-content:center;border-radius:22px;font-weight:600;font-size:12px;white-space:nowrap}
.btn-dark{position:absolute;left:548px;width:95px;height:28px;background:var(--navy);color:var(--white);font-size:10px}
.btn-light{position:absolute;left:651px;width:80px;height:28px;background:var(--white);color:var(--ink);font-size:10px;box-shadow:0 4px 10px rgba(38,42,72,.12)}
.btn-blue{background:var(--blue);color:var(--white);box-shadow:0 8px 18px rgba(27,147,209,.3)}
.hero-title{left:235px;top:194px;font-size:33px;font-weight:700;line-height:44px;width:420px;white-space:nowrap}
.para{font-size:13px;line-height:20px;color:var(--text)}
.center{text-align:center}
.placeholder{border-radius:6px;background:linear-gradient(160deg,#fbfcfe,#eef2f8);border:1px solid var(--line);box-shadow:0 18px 40px rgba(38,42,72,.12)}
.section-title{font-size:30px;font-weight:500;line-height:36px;width:1200px;text-align:center}
.feature{position:absolute;width:250px;text-align:center}
.feature-box{width:86px;height:86px;margin:0 auto;border-radius:4px;display:flex;align-items:center;justify-content:center;background:var(--white);box-shadow:0 10px 24px rgba(38,42,72,.1)}
.feature-box.active{background:var(--blue-deep)}
.feature h3{font-size:16px;font-weight:600;margin-top:48px}
.feature p{margin-top:8px;font-size:12px;line-height:16px;color:var(--text)}
.row-title{font-size:26px;font-weight:700;line-height:30px;width:300px}
.row-btn{width:126px;height:35px;font-size:12px}
.stat{position:absolute;width:200px;text-align:center}
.stat-icon{width:70px;height:70px;margin:0 auto;display:flex;align-items:center;justify-content:center;border-radius:42% 58% 50% 50%/55% 45% 55% 45%;background:#e8eef8}
.stat-num{font-size:34px;color:var(--blue);margin-top:14px;line-height:40px}
.stat-label{font-size:19px;color:var(--text);line-height:24px}
.card{left:445px;top:3255px;width:313px;height:337px;background:var(--white);border-radius:14px;box-shadow:0 16px 44px rgba(38,42,72,.12)}
.footer{left:0;top:3716px;width:1200px;height:329px;background:var(--navy)}
.field{position:absolute;height:36px;border-radius:20px;background:var(--white);font-size:10px;color:#b3b7c6;padding:0 18px;display:flex;align-items:center}
.foot-links{position:absolute;left:690px;top:3962px;display:flex;gap:16px;font-size:12px;font-weight:600;color:var(--white);white-space:nowrap}
</style>
</head>
<body>

<svg class="bg-wave" style="top:1080px" height="1400" viewBox="0 0 1200 1400" aria-hidden="true">
  <path d="M0 40 C300 -20 600 80 1200 20 L1200 520 C800 600 400 460 0 560Z" fill="#f7f8fc"/>
  <path d="M0 520 C400 440 800 560 1200 480 L1200 980 C800 1060 400 940 0 1000Z" fill="#f9fafd"/>
  <path d="M0 900 C300 960 700 860 1200 940 L1200 1360 C700 1300 400 1400 0 1340Z" fill="#f7f8fc"/>
</svg>
<svg class="bg-wave" style="top:2480px" height="760" viewBox="0 0 1200 760" aria-hidden="true">
  <path d="M0 120 C350 40 700 160 1200 60 L1200 560 C800 640 300 520 0 620Z" fill="#f5f7fb"/>
</svg>

<svg class="hero-blob" width="1200" height="460" viewBox="0 0 1200 460" aria-hidden="true">
  <defs><linearGradient id="heroGrad" x1="0" y1="0" x2="1" y2="1"><stop offset="0" stop-color="#1c9bd8"/><stop offset="1" stop-color="#0f7ec0"/></linearGradient></defs>
  <path d="M545 0 L1200 0 L1200 400 C1100 450 960 430 870 360 C760 270 720 150 640 80 C590 45 560 20 545 0Z" fill="url(#heroGrad)"/>
</svg>

<header class="header">
  <div class="logo"><span class="logo-square"></span>Brixel Software</div>
  <nav class="nav"><span>Home</span><span>About</span><span>Our Solutions</span><span>Blog</span><span>Login</span><span>SignUp</span></nav>
  <span class="btn btn-dark">Request a Demo</span>
  <span class="btn btn-light">Contact Us</span>
</header>

<h1 class="abs hero-title">Cras neque aliquam<br>portitor vitae.</h1>
<p class="abs para" style="left:235px;top:310px;width:340px">Vestibulum mi massa, tempor in massa quis, tristique gravida massa. Sed quis commodo nibh.</p>
<span class="abs btn btn-blue" style="left:235px;top:396px;width:123px;height:36px">Request a Demo</span>

<div class="abs placeholder" role="img" aria-label="Laptop showing the Brixel dashboard" style="left:599px;top:210px;width:418px;height:280px;border:10px solid #ffffff"></div>
<div class="abs" style="left:526px;top:482px;width:561px;height:12px;border-radius:0 0 20px 20px;background:#eef1f6;box-shadow:0 6px 14px rgba(38,42,72,.08)"></div>

<h2 class="abs section-title" style="left:0;top:602px">Let's Get Started<br>Learn more About Our Concept</h2>
<p class="abs para center" style="left:300px;top:694px;width:600px;font-size:11px;line-height:15px">Ut sit amet rutrum mi, et convallis enim. Sed nisl tortor, viverra at consectetur sit amet, ultrices eu leo. Ut ut dapibus neque. In porta justo tellus quis porttitor est aliquet nec.</p>
<p class="abs para center" style="left:300px;top:740px;width:600px;font-size:11px;line-height:15px">Fusce felis tellus, vestibulum sed viverra et, luctus id arcu. Nulla nec, aliquam felis. Nam a porta massa. Etiam porttitor lectus in ipsum, sollicitudin ipsum consectetur.</p>

<div class="feature" style="left:225px;top:855px">
  <div class="feature-box active"><svg width="40" height="40" viewBox="0 0 40 40" fill="none" stroke="#fff" stroke-width="2"><path d="M8 32h24M12 32V18h16v14M10 18l10-8 10 8M17 24h6v8h-6z"/></svg></div>
  <h3>Fast &amp; Optimized</h3><p>Mauris non felis eu nunc<br>tincidunt luctus sed ut ligula.</p>
</div>
<div class="feature" style="left:475px;top:855px">
  <div class="feature-box"><svg width="40" height="40" viewBox="0 0 40 40" fill="none" stroke="#8a90a6" stroke-width="2"><rect x="7" y="8" width="26" height="24" rx="2"/><path d="M7 14h26M12 20h10M12 25h16"/></svg></div>
  <h3>Easy to control</h3><p>Mauris non felis eu nunc<br>tincidunt luctus sed ut ligula.</p>
</div>
<div class="feature" style="left:725px;top:855px">
  <div class="feature-box"><svg width="40" height="40" viewBox="0 0 40 40" fill="none" stroke="#8a90a6" stroke-width="2"><rect x="10" y="6" width="18" height="28" rx="2"/><path d="M15 14h8M15 19h8M15 24h5"/></svg></div>
  <h3>Smartphone compatible</h3><p>Mauris non felis eu nunc<br>tincidunt luctus sed ut ligula.</p>
</div>

<div class="abs placeholder" role="img" aria-label="Brixel dashboard with charts and a world map" style="left:235px;top:1173px;width:356px;height:270px"></div>
<h2 class="abs row-title" style="left:672px;top:1192px">Vivamus imperdiet massa lobortis</h2>
<p class="abs para" style="left:672px;top:1277px;width:290px;font-size:11px;line-height:15px">Donec viverra mi vel fermentum maximus. Vivamus ultrices nisl eu velit efficitur consequat. Donec nec venenatis nisl. Risus eget venenatis posuere.</p>
<span class="abs btn btn-blue row-btn" style="left:672px;top:1375px">Read More</span>

<h2 class="abs row-title" style="left:235px;top:1660px">Nam scelerisque maximus nibh</h2>
<p class="abs para" style="left:235px;top:1745px;width:290px;font-size:11px;line-height:15px">Donec viverra mi vel fermentum maximus. Vivamus ultrices nisl eu velit efficitur consequat. Donec nec venenatis nisl. Risus eget venenatis posuere.</p>
<span class="abs btn btn-blue row-btn" style="left:235px;top:1845px">Read More</span>
<div class="abs placeholder" role="img" aria-label="Brixel dashboard with charts and a world map" style="left:610px;top:1642px;width:356px;height:273px"></div>

<div class="abs placeholder" role="img" aria-label="Brixel dashboard with charts and a world map" style="left:235px;top:2069px;width:356px;height:269px"></div>
<h2 class="abs row-title" style="left:672px;top:2085px">Etiam tellus enim, suscipit sit amet</h2>
<p class="abs para" style="left:672px;top:2168px;width:290px;font-size:11px;line-height:15px">Donec viverra mi vel fermentum maximus. Vivamus ultrices nisl eu velit efficitur consequat. Donec nec venenatis nisl. Risus eget venenatis posuere.</p>
<span class="abs btn btn-blue row-btn" style="left:672px;top:2268px">Read More</span>

<h2 class="abs section-title" style="left:0;top:2580px;font-size:26px;line-height:33px">Vestibulum vel velit facilisis, condimentum neque.<br>Pellentesque tortor augue</h2>
<p class="abs para center" style="left:330px;top:2686px;width:540px;font-size:11px;line-height:15px">Ut sit amet rutrum mi, et convallis enim. Sed nisl tortor, viverra at consectetur sit amet, ultrices eu leo. Ut ut dapibus neque. In porta justo tellus quis porttitor est aliquet nec. Fusce felis tellus, vestibulum sed viverra et, luctus id arcu. Nulla nec felis. Nam a porta massa. Etiam porttitor lectus in ipsum, sollicitudin ipsum consectetur.</p>

<div class="stat" style="left:183px;top:2797px">
  <div class="stat-icon"><svg width="26" height="26" viewBox="0 0 26 26" fill="none" stroke="#262a48" stroke-width="1.6"><circle cx="13" cy="11" r="6"/><path d="M10 20h6M11 23h4"/></svg></div>
  <div class="stat-num">84%</div><div class="stat-label">Creativity</div>
</div>
<div class="stat" style="left:404px;top:2797px">
  <div class="stat-icon"><svg width="26" height="26" viewBox="0 0 26 26" fill="none" stroke="#262a48" stroke-width="1.6"><path d="M8 8l-5 5 5 5M18 8l5 5-5 5M15 5l-4 16"/></svg></div>
  <div class="stat-num">90%</div><div class="stat-label">Development</div>
</div>
<div class="stat" style="left:623px;top:2797px">
  <div class="stat-icon"><svg width="26" height="26" viewBox="0 0 26 26" fill="none" stroke="#262a48" stroke-width="1.6"><circle cx="13" cy="8" r="4"/><path d="M6 23v-6a7 7 0 0 1 14 0v6"/></svg></div>
  <div class="stat-num">126</div><div class="stat-label">Satisfied Customer</div>
</div>
<div class="stat" style="left:812px;top:2797px">
  <div class="stat-icon"><svg width="26" height="26" viewBox="0 0 26 26" fill="none" stroke="#262a48" stroke-width="1.6"><circle cx="13" cy="10" r="6"/><path d="M9 15l-2 8 6-3 6 3-2-8"/></svg></div>
  <div class="stat-num">06</div><div class="stat-label">Earned Trophy</div>
</div>

<p class="abs center" style="left:0;top:3117px;width:1200px;font-size:11px;letter-spacing:1px;color:#b4b8c8">TESTIMONIALS</p>
<h2 class="abs section-title" style="left:0;top:3142px;font-size:30px;font-weight:600">Check what people say<br>About us!</h2>
<div class="abs card">
  <svg class="abs" style="left:32px;top:34px" width="32" height="26" viewBox="0 0 32 26" fill="#c8ccd8" aria-hidden="true"><path d="M0 26V14C0 6 4 1 12 0v5c-4 1-6 4-6 8h6v13zM18 26V14c0-8 4-13 12-14v5c-4 1-6 4-6 8h6v13z"/></svg>
  <p class="abs para center" style="left:30px;top:92px;width:253px;font-size:12px;line-height:17px">"Excepteur sint occaecat cupida non at proident, sunt culp officia deserun moli anim est laborum. Sed perspi unde omnis iste natus error sit voluptatem accusantium doloremque laudantium"</p>
  <div class="abs" style="left:32px;top:280px;width:34px;height:34px;border-radius:50%;background:var(--navy)" role="img" aria-label="Customer portrait"></div>
  <p class="abs" style="left:80px;top:282px;font-size:13px;font-weight:600;color:var(--blue)">Mira Lane</p>
  <p class="abs" style="left:80px;top:300px;font-size:9px;color:var(--text)">Customer</p>
</div>
<div class="abs" style="left:588px;top:3638px;display:flex;gap:5px">
  <span style="width:6px;height:6px;border-radius:50%;background:var(--navy)"></span><span style="width:6px;height:6px;border-radius:50%;background:var(--navy)"></span><span style="width:6px;height:6px;border-radius:50%;background:var(--navy)"></span>
</div>

<footer class="abs footer">
  <h2 class="abs center" style="left:0;top:57px;width:1200px;font-size:30px;font-weight:500;color:var(--white)">Subscribe Our Newsletter</h2>
  <div class="field" style="left:297px;top:133px;width:224px">Full Name</div>
  <div class="field" style="left:537px;top:133px;width:220px">Email Address</div>
  <span class="abs btn btn-blue" style="left:774px;top:133px;width:130px;height:36px;font-size:10px;box-shadow:none">SIGN UP NOW</span>
  <div class="abs logo" style="left:235px;top:238px;color:var(--white);font-size:20px"><span class="logo-square"></span>Brixel Software</div>
  <p class="abs" style="left:235px;top:280px;font-size:11px;color:var(--white)">All Right Reserved 2019 <span style="color:var(--blue)">Brixel Software</span></p>
  <div class="abs" style="left:884px;top:284px;display:flex;gap:14px">
    <span style="width:9px;height:9px;border-radius:50%;background:#5d6385"></span><span style="width:9px;height:9px;border-radius:50%;background:#5d6385"></span><span style="width:9px;height:9px;border-radius:50%;background:#5d6385"></span><span style="width:9px;height:9px;border-radius:50%;background:#5d6385"></span>
  </div>
</footer>
<nav class="foot-links"><span>Home</span><span>About</span><span>Our Solutions</span><span>Blog</span><span>Contact Us</span></nav>

</body>
</html>
```